Vesit cards for web development company

We need a business card design for our company. The company develops online platforms and conducts marketing consulting. Company logo. The cards must fit in with us (a junior start UP), but they must also be professional enough to impress with investors like banks. We wish you a combination of classic and modern design

Target Market(s)

Business partners and IT and marketing customers

Industry/Entity Type

It Company

Contact Information for Business Card

Folgende Information müssen Drauf.
Name, Position, Telefon Nr., Mobile Nr., E-Mail adresse, Optional sind noch Webadresse und HRB Nummer

Colors

Designer to choose colors to be used in the design.

Requirements
Must have
• The cards have to fit into the logo later and have to be dynamic and serious at the same time

```html
<!DOCTYPE html>
<html lang="en">
<head>
<meta charset="utf-8">
<title>Nordwerk Digital – Business Card</title>
<link href="https://fonts.googleapis.com/css2?family=Open+Sans:wght@400;600;700&display=swap" rel="stylesheet">
<style>
  :root {
    --page-bg: #ecebe8;
    --card-dark: #3a3a3c;
    --card-light: #ffffff;
    --brand-blue: #3f7fd0;
    --text-grey: #6b6b6b;
    --text-dark: #555555;
  }
  * { box-sizing: border-box; margin: 0; padding: 0; }
  html, body { width: 1200px; height: 800px; overflow: hidden; }
  body {
    background: var(--page-bg);
    font-family: "Open Sans", Arial, sans-serif;
    display: flex;
    align-items: center;
    justify-content: center;
    gap: 40px;
  }
  .card {
    width: 540px;
    height: 310px;
    border-radius: 22px;
    position: relative;
    box-shadow: 0 6px 18px rgba(0,0,0,0.18);
    overflow: hidden;
  }
  .card-front {
    background: var(--card-dark);
    display: flex;
    align-items: center;
    justify-content: center;
  }
  .brand {
    display: flex;
    align-items: center;
    gap: 12px;
  }
  .brand-dot {
    width: 22px;
    height: 22px;
    border-radius: 50%;
    background: var(--brand-blue);
  }
  .brand-name {
    font-weight: 700;
    color: var(--brand-blue);
    text-transform: uppercase;
    letter-spacing: 1.5px;
  }
  .card-front .brand-name { font-size: 34px; }
  .card-back { background: var(--card-light); }
  .card-back .brand {
    position: absolute;
    top: 44px;
    right: 56px;
    gap: 8px;
  }
  .card-back .brand-dot { width: 14px; height: 14px; }
  .card-back .brand-name { font-size: 20px; }
  .holder {
    position: absolute;
    left: 0;
    top: 118px;
    padding-left: 22px;
    border-left: 8px solid var(--brand-blue);
  }
  .holder-name {
    font-size: 24px;
    color: var(--text-grey);
    font-weight: 400;
    line-height: 1.1;
  }
  .holder-name strong { font-weight: 700; }
  .holder-title {
    font-size: 14px;
    color: var(--brand-blue);
  }
  .contacts {
    position: absolute;
    left: 30px;
    bottom: 38px;
    list-style: none;
    font-size: 15px;
    color: var(--text-dark);
    line-height: 1.55;
  }
  .contacts li { display: flex; align-items: center; gap: 10px; }
  .contacts svg { width: 14px; height: 14px; fill: var(--brand-blue); }
  .footer-rule {
    position: absolute;
    left: 30px;
    bottom: 22px;
    width: 330px;
    height: 2px;
    background: var(--brand-blue);
  }
  .website {
    position: absolute;
    right: 30px;
    bottom: 14px;
    font-size: 13px;
    color: var(--brand-blue);
  }
</style>
</head>
<body>
  <section class="card card-front">
    <div class="brand">
      <span class="brand-dot"></span>
      <span class="brand-name">Nordwerk Digital</span>
    </div>
  </section>

  <section class="card card-back">
    <div class="brand">
      <span class="brand-dot"></span>
      <span class="brand-name">Nordwerk Digital</span>
    </div>

    <div class="holder">
      <p class="holder-name">Your <strong>Name</strong></p>
      <p class="holder-title">Job title</p>
    </div>

    <ul class="contacts">
      <li>
        <svg viewBox="0 0 16 16" aria-hidden="true"><path d="M3 1h3l1.5 4-2 1.2a9 9 0 0 0 4.3 4.3L11 8.5l4 1.5v3a2 2 0 0 1-2 2A13 13 0 0 1 1 3a2 2 0 0 1 2-2z"/></svg>
        000 000 0000
      </li>
      <li>
        <svg viewBox="0 0 16 16" aria-hidden="true"><path d="M4 1h8a1 1 0 0 1 1 1v12a1 1 0 0 1-1 1H4a1 1 0 0 1-1-1V2a1 1 0 0 1 1-1zm1 2v9h6V3z"/></svg>
        000 000 0000
      </li>
      <li>
        <svg viewBox="0 0 16 16" aria-hidden="true"><path d="M1 3h14v10H1zm1.5 1.2v.3L8 9l5.5-4.5v-.3z"/></svg>
        youremail@xyz.com
      </li>
    </ul>

    <div class="footer-rule"></div>
    <p class="website">www.yourwebsite.com</p>
  </section>
</body>
</html>
```